Oversized Postcard for Estate Planning & Probate 1st 2nd and 3rd prizes

Create a professional, fresh and polished oversized post card for law firm specializing in Estate Planning & Probate Law for High Net Worth Clients

Use any picture(s) of your choice (mine or ones you recommend), logo, headshot and company info

www.morvenashbylaw.com

Westbrook Office - 4700 Kestrel Avenue, Suite 1400, Charlotte, NC 28210
Harrowgate Office - 13540 Birch Court, Suite 300, Charlotte, NC 28277

Phone (704) 555-0187

Use this card for a Free Consultation

Target Market(s)

young and old families too; business owners

Industry/Entity Type

Law Firm

Font styles to use
Serif
Sans Serif

Requirements
Must have
• Use any picture(s) of your choice (mine or ones you recommend), logo, headshot and company info
• www.morvenashbylaw.com
• Westbrook Office - 4700 Kestrel Avenue, Suite 1400, Charlotte, NC 28210
• Harrowgate Office - 13540 Birch Court, Suite 300, Charlotte, NC 28277
• Phone (704) 555-0187
• Use this card for a Free Consultation
Nice to have
• great colors and great design; like graphics with depth /shading
Should not have
• don't use too many pics - keep it simple

```html
<!DOCTYPE html>
<html lang="en">
<head>
<meta charset="utf-8">
<title>Morven Ashby Law PLLC – Postcard</title>
<link rel="stylesheet" href="https://fonts.googleapis.com/css2?family=Open+Sans:wght@400;600;700&family=Mulish:wght@400&family=Crimson+Text:ital@1&display=swap">
<style>
:root{
  --navy:#0b4060;
  --deep:#0b4566;
  --teal:#13607f;
  --sky:#5bc0ea;
  --brand:#0d5c85;
  --phone:#2f7ea6;
  --paper:#f4f8fb;
  --slot:#e5ecf4;
  --ink:#1b2630;
  --bg:#e9e6e2;
}
*{margin:0;padding:0;box-sizing:border-box}
html,body{width:904px;height:1200px;overflow:hidden;background:var(--bg)}
body{position:relative;font-family:"Open Sans",sans-serif}
.card{position:absolute;left:50px;width:808px;height:524px;overflow:hidden;background:var(--paper);box-shadow:0 4px 14px rgba(0,0,0,.25)}
.front{top:60px}
.back{top:610px;background:#fff}
.abs{position:absolute}

/* front */
.front-panel{position:absolute;left:0;top:0}
.headshot{left:92px;top:12px;width:180px;height:208px;border-radius:90px 90px 0 0;background:linear-gradient(180deg,#d9c39a 0%,#c9a878 45%,#1d2228 80%)}
.intro{left:80px;top:222px;width:229px;color:#fff;font-family:"Mulish",sans-serif;font-size:12px;line-height:17.6px;text-align:justify;text-align-last:center}
.front-phone{left:80px;top:392px;width:236px;text-align:center;color:#fff;font-size:24px;font-weight:600}
.sign-name{left:120px;top:444px;width:190px;text-align:center;color:rgba(255,255,255,.25);font-family:"Crimson Text",serif;font-style:italic;font-size:16px}
.offer{left:150px;top:470px;width:130px;text-align:center;color:#fff;font-family:"Crimson Text",serif;font-style:italic;font-size:12.5px;line-height:17.6px}
.family-photo{left:382px;top:164px;width:426px;height:360px;background:linear-gradient(180deg,rgba(244,248,251,0) 0%,#e6d8c3 35%,#d2c0a6 65%,#b9d4e2 100%)}
.logo-box{left:478px;top:24px;width:244px;height:148px;background:#fff}
.logo-dot{left:562px;top:28px;width:72px;height:72px;border-radius:50%;background:var(--teal)}
.logo-name{left:478px;top:110px;width:244px;text-align:center;color:var(--brand);font-size:21px;font-weight:600;line-height:26px}
.logo-sub{left:478px;top:136px;width:244px;text-align:center;color:var(--brand);font-size:21px;font-weight:600;line-height:26px}
.tagline{left:455px;top:418px;width:340px;text-align:center;color:var(--ink);font-size:15.5px;line-height:25px;letter-spacing:-.2px}
.front-web{left:440px;top:474px;width:360px;text-align:center;color:var(--brand);font-size:25px;font-weight:700}

/* back */
.band{left:0;top:0;width:808px;height:160px;background:var(--navy)}
.services{left:29px;top:22px;list-style:none;color:#fff;font-size:16px;line-height:27px;columns:2;column-gap:16px;width:380px}
.services li{display:flex;align-items:center;gap:8px;break-inside:avoid}
.services li::before{content:"";width:12px;height:12px;border-radius:50%;background:radial-gradient(circle at 35% 35%,#9fdcff,#1c7fc0)}
.kids-photo{left:0;top:160px;width:538px;height:364px;background:linear-gradient(135deg,#bcd9e8 0%,#f3ecc9 40%,#e7c9a4 70%,#c9dfe6 100%)}
.wedges{left:354px;top:160px;z-index:2}
.offices{left:374px;top:0;width:218px;height:182px;background:var(--teal);color:#fff;text-align:center;z-index:3}
.office{position:absolute;left:0;width:218px}
.office h3{font-size:18px;font-weight:600;line-height:24px}
.office p{font-size:12.5px;line-height:17px;margin-top:4px}
.office.one{top:20px}
.office.two{top:104px}
.office-rule{position:absolute;left:0;top:94px;width:218px;height:4px;background:#fff}
.postage{left:678px;top:13px;width:117px;height:117px;background:var(--slot);display:flex;align-items:center;justify-content:center;text-align:center;font-family:Arial,sans-serif;font-size:14px;color:#111}
.back-dot{left:24px;top:174px;width:104px;height:104px;border-radius:50%;background:var(--teal);border:3px solid #1b2630}
.back-name{left:138px;top:214px;color:var(--navy);font-size:15px;font-weight:600}
.back-phone{left:138px;top:166px;color:var(--phone);font-size:24px;font-weight:600}
.email{left:380px;top:184px;color:#555;font-size:15px;font-family:"Mulish",sans-serif;z-index:3}
.address{left:538px;top:230px;width:257px;height:280px;background:var(--slot);padding-top:54px;text-align:center;font-family:Arial,sans-serif;font-size:15px;color:#111}
.barcode{left:350px;top:453px;width:445px;height:57px;background:var(--slot);display:flex;align-items:center;justify-content:center;font-family:Arial,sans-serif;font-size:15px;color:#111}
.back-web{left:43px;top:485px;color:var(--navy);font-size:21px;font-weight:700}
</style>
</head>
<body>

<section class="card front">
  <div class="abs family-photo" role="img" aria-label="Photo of a smiling three-generation family on a beach"></div>
  <svg class="front-panel" width="420" height="524" viewBox="0 0 420 524" aria-hidden="true">
    <defs>
      <linearGradient id="swoosh" x1="0" y1="0" x2="1" y2="0">
        <stop offset="0" stop-color="#1a6ea0"/>
        <stop offset="1" stop-color="#5bc0ea"/>
      </linearGradient>
    </defs>
    <path d="M0 0H360C430 150 430 380 300 524H0Z" fill="url(#swoosh)"/>
    <path d="M0 0H330C400 150 400 380 280 524H0Z" fill="#0e3d5c"/>
    <path d="M0 0H318C385 150 385 380 268 524H0Z" fill="#1484ab"/>
    <path d="M80 0H305C372 150 370 380 240 524H90C40 380 30 140 80 0Z" fill="var(--deep)"/>
    <path d="M58 0C20 150 25 380 82 524" fill="none" stroke="#5bc0ea" stroke-width="5"/>
  </svg>
  <div class="abs headshot" role="img" aria-label="Headshot of the attorney"></div>
  <p class="abs intro">Morven Ashby Law, PLLC serving clients in estate planning, estate administration, probate law, wills, revocable trusts, irrevocable trusts, powers of attorney, health care powers of attorney, living wills, hipaa releases, guardianships, special needs planning, wealth transfers, elder law and business law in North Carolina and South Carolina.</p>
  <div class="abs front-phone">(704) 555-0187</div>
  <div class="abs sign-name">Morven Ashby</div>
  <p class="abs offer">Use this card for a<br>Free Consultation</p>

  <div class="abs logo-box"></div>
  <div class="abs logo-dot"></div>
  <div class="abs logo-name">Morven Ashby</div>
  <div class="abs logo-sub">Law PLLC</div>

  <p class="abs tagline">SERVING CLIENTS WITH COMPASSION AND<br>LEGAL GUIDANCE IS OUR PASSION...</p>
  <div class="abs front-web">www.morvenashbylaw.com</div>
</section>

<section class="card back">
  <div class="abs band"></div>
  <ul class="abs services">
    <li>Estate Administration</li>
    <li>Estate Planning</li>
    <li>Trusts</li>
    <li>Healthcare Powers</li>
    <li>Probate Law</li>
    <li>Wills</li>
    <li>Living Wills</li>
  </ul>
  <div class="abs postage">Postage<br>Area</div>

  <div class="abs kids-photo" role="img" aria-label="Photo of a laughing young family with two boys outdoors"></div>
  <svg class="abs wedges" width="270" height="26" viewBox="0 0 270 26" aria-hidden="true">
    <path d="M0 0H20V22Z" fill="var(--navy)"/>
    <path d="M238 0H270L238 26Z" fill="var(--navy)"/>
  </svg>
  <div class="abs offices">
    <div class="office one">
      <h3>Westbrook Office</h3>
      <p>4700 Kestrel Avenue, Suite 1400,<br>Charlotte, NC 28210</p>
    </div>
    <div class="office-rule"></div>
    <div class="office two">
      <h3>Harrowgate Office</h3>
      <p>13540 Birch Court, Suite 300,<br>Charlotte, NC 28277</p>
    </div>
  </div>
  <div class="abs back-dot"></div>
  <div class="abs back-phone">(704) 555-0187</div>
  <div class="abs back-name">Morven Ashby Law PLLC</div>
  <div class="abs email">morven@morvenashbylaw.com</div>
  <div class="abs address">Address Area</div>
  <div class="abs barcode">Barcode Area</div>
  <div class="abs back-web">www.morvenashbylaw.com</div>
</section>

</body>
</html>
```